VELVET ORBITS - BOOK COVER

I have written a book called VELVET ORBIT - HOW TO CLIMB PAST EVERY LIMIT TO THE TOP RUNG. I need a front cover design for the book. The book cover needs to be intriguing for someone to pick it up and read the first couple of pages. I want people to think about ACHIEVING SUCCESS when they read this book.
PLEASE LOOK AT THE ATTACHMENT. THANKS!

Target Market(s)

males, entrepreneurs, small business owners, salespeople, corporate executives

Industry/Entity Type

Business

Logo Text

VELVET ORBITS

Logo styles of interest
Emblem Logo
Abstract Logo
Font styles to use
Serif
Sans Serif

Colors
ec1f27
000000
959595
ffffff

Requirements
Must have
• It has to have a "hurricane" feel to it with hurricane colors.
Nice to have
• I open to your ideas
Should not have
• no other colors except red, black, gray, white.

```html
<!DOCTYPE html>
<html lang="en">
<head>
<meta charset="utf-8">
<title>Velvet Orbits – Book Cover</title>
<link rel="stylesheet" href="https://fonts.googleapis.com/css2?family=Poppins:wght@400;500&family=Exo+2:ital,wght@1,800&display=swap">
<style>
  :root {
    --paper: #e7e8e9;
    --swirl: #c9cacc;
    --swirl-soft: #d6d7d9;
    --red: #ec1f27;
    --deep-red: #c41e2e;
    --ink: #000000;
    --white: #ffffff;
  }
  html, body {
    margin: 0;
    padding: 0;
    width: 1200px;
    height: 1096px;
    overflow: hidden;
    background: var(--paper);
  }
  .cover {
    position: relative;
    width: 1200px;
    height: 1096px;
    background: var(--paper);
    overflow: hidden;
    font-family: "Poppins", sans-serif;
    color: var(--ink);
  }
  .swirl-backdrop {
    position: absolute;
    inset: 0;
    background:
      radial-gradient(circle at 52% 50%,
        var(--swirl-soft) 0 18%,
        var(--swirl) 18% 26%,
        var(--swirl-soft) 26% 34%,
        var(--swirl) 34% 46%,
        var(--swirl-soft) 46% 56%,
        var(--swirl) 56% 68%,
        var(--paper) 68% 100%);
  }
  .storm-art {
    position: absolute;
    left: 450px;
    top: 200px;
    width: 310px;
    height: 450px;
    border-radius: 48% 48% 40% 40% / 30% 30% 70% 70%;
    background: linear-gradient(180deg, var(--white) 0%, var(--deep-red) 45%, var(--white) 100%);
    opacity: 0.9;
  }
  .series-name {
    position: absolute;
    top: 88px;
    left: 0;
    width: 100%;
    text-align: center;
    font-size: 31px;
    font-weight: 400;
    letter-spacing: 0.5px;
    margin: 0;
  }
  .subtitle-lead {
    position: absolute;
    top: 708px;
    left: 0;
    width: 100%;
    text-align: center;
    margin: 0;
    font-family: "Exo 2", sans-serif;
    font-style: italic;
    font-weight: 800;
    font-size: 42px;
    letter-spacing: 2px;
    color: var(--deep-red);
  }
  .subtitle-tail {
    position: absolute;
    top: 896px;
    left: 0;
    width: 100%;
    text-align: center;
    margin: 0;
    font-size: 34px;
    font-weight: 400;
    letter-spacing: 0.5px;
  }
  .author {
    position: absolute;
    top: 980px;
    left: 0;
    width: 100%;
    text-align: center;
    margin: 0;
    font-size: 23px;
    font-weight: 400;
    letter-spacing: 0.5px;
  }
</style>
</head>
<body>
  <main class="cover">
    <div class="swirl-backdrop" role="img" aria-label="Large soft grey hurricane spiral pattern filling the background"></div>
    <h1 class="series-name">VELVET ORBITS</h1>
    <div class="storm-art" role="img" aria-label="Red and white swirling hurricane funnel illustration"></div>
    <h2 class="subtitle-lead">HOW TO CLIMB PAST EVERY LIMIT</h2>
    <p class="subtitle-tail">TO THE TOP RUNG</p>
    <p class="author">BY MARA DELLQUIST</p>
  </main>
</body>
</html>
```